KM Rivergate Fitness personal training needs a new Business Card design for 2016

Business Card design:
Our current business card is very plain
We are bringing on our first team member next year and thought its a perfect time to have a new face lift for our company!

We are a Personal Training business "KM Rivergate Fitness" who specializes in strength and conditioning / weightloss training,
We also run a yearly Bootcamp called "Thunderpeak Bootcamps", this is our Logo Design which we are looking for

The pink and blue in the logo are our business colours, how ever we don't want those colours to heavily dominate the card.

We are looking for a business card which is eye catching, and creative.

I am open to suggestions and any designs :)

Logo Design:

For our Logo Design we are looking for a bright, energetic logo, preferably a word logo which portrays strength and high intensity
If it has icon's etc in it thats fine again im open for suggestions :)
The Logo Design is for our Bootcamp which runs yearly
The bootcamp is called "Thunderpeak Bootcamp"

Target Market(s)

Age 20-40
Individuals who want to look great and have more energy

Industry/Entity Type

Business

Contact Information for Business Card

On the front
KM Rivergate Fitness Kemal Mortby Personal Training / Bootcamps / Pilates / Nutrition Healthy mind, Healthy body, Ultimate lifestyle < our slogan
Icons for the following
Email:
Mobile:
Facebook:
Instagram:

On the back we would like to include somewhere
"Show this card to receive 50% off your first 30min pt session"
"Valid to one user only"

Logo Text

Thunderpeak Bootcamp

Font styles to use
Serif

Colors
e34197
0255a3
000000
ffffff

Requirements
Must have
• - Icons for instagram, facebook, email and mobile phone
• - Slogan: Healthy mind, Healthy body, Ultimate lifestyle
• - What we offer: Personal Training , Bootcamps, Pilates, Nutrition
• - Logo
Nice to have
• - Our 50% offer on the back
• - a place for a photo
Should not have
• - Pink and Blue everywhere

```html
<!DOCTYPE html>
<html lang="en">
<head>
<meta charset="utf-8">
<title>KM Rivergate Fitness – Business Card</title>
<link rel="stylesheet" href="https://fonts.googleapis.com/css2?family=Exo+2:wght@700;800&family=Open+Sans:wght@400;600&display=swap">
<style>
  :root {
    --blue: #0255a3;
    --blue-light: #2a86cf;
    --blue-mid: #1a6fbf;
    --pink: #e34197;
    --pink-soft: #e58cc0;
    --ink: #1b1b1b;
    --white: #ffffff;
    --paper: #f4f4f4;
    --stage: #e7e9ec;
  }
  * { box-sizing: border-box; margin: 0; padding: 0; }
  html, body { width: 1200px; height: 780px; overflow: hidden; }
  body {
    background: var(--stage);
    display: flex; align-items: center; justify-content: center; gap: 40px;
    font-family: "Open Sans", Arial, sans-serif;
  }
  .card {
    position: relative; width: 540px; height: 300px; overflow: hidden;
    box-shadow: 0 6px 18px rgba(0,0,0,.18);
  }

  /* Front */
  .card-front { background: var(--paper); }
  .card-front .waves { position: absolute; inset: 0; }
  .holder { position: absolute; right: 215px; top: 26px; text-align: right; }
  .holder-name {
    font-family: "Exo 2", Arial, sans-serif; font-weight: 700;
    color: var(--blue-mid); font-size: 19px; letter-spacing: .5px; line-height: 1.2;
    white-space: nowrap;
  }
  .holder-role { color: var(--ink); font-size: 12px; line-height: 1.3; }
  .brand { position: absolute; left: 24px; top: 120px; display: flex; align-items: center; gap: 12px; }
  .brand-dot { width: 58px; height: 58px; border-radius: 50%; background: var(--blue-mid); flex: none; }
  .brand-name {
    font-family: "Exo 2", Arial, sans-serif; font-weight: 800;
    color: var(--blue-mid); font-size: 22px; line-height: 1.05; text-transform: uppercase;
  }
  .slogan { position: absolute; left: 94px; top: 186px; color: var(--ink); font-size: 11.5px; line-height: 1.35; }
  .slogan span { display: block; }
  .slogan span + span { padding-left: 34px; }
  .contacts {
    position: absolute; right: 16px; top: 70px; list-style: none;
    color: var(--white); font-size: 11px; text-align: right; line-height: 1.5;
  }
  .contacts li { display: flex; justify-content: flex-end; align-items: center; gap: 6px; white-space: nowrap; }
  .contacts svg { width: 11px; height: 11px; flex: none; }
  .contacts .address { padding-right: 17px; }

  /* Back */
  .card-back {
    background: radial-gradient(ellipse at 50% 35%, var(--blue-light), var(--blue) 95%);
    color: var(--white); text-align: center; padding-top: 30px;
  }
  .back-brand {
    font-family: "Exo 2", Arial, sans-serif; font-weight: 800;
    font-size: 40px; line-height: 1; letter-spacing: 1px; text-transform: uppercase;
  }
  .back-brand span { display: block; font-size: 26px; letter-spacing: 6px; margin-top: 2px; }
  .offer { color: var(--pink-soft); font-size: 12.5px; font-weight: 600; margin-top: 14px; }
  .valid { font-size: 22px; font-weight: 600; margin-top: 8px; }
  .services-label { font-size: 17px; font-weight: 600; margin-top: 4px; }
  .services { font-size: 12.5px; margin-top: 6px; }
  .website { font-size: 12.5px; font-weight: 600; margin-top: 6px; }
</style>
</head>
<body>

<section class="card card-front" aria-label="Business card front">
  <svg class="waves" viewBox="0 0 540 300" aria-hidden="true">
    <path d="M295 130 C290 220 220 270 135 300 L180 300 C265 265 310 205 313 130 Z" fill="var(--pink-soft)"/>
    <path d="M360 0 C300 70 345 150 305 225 C280 270 240 290 205 300 L540 300 L540 0 Z" fill="var(--blue-mid)"/>
    <path d="M385 0 C330 60 365 150 322 230 C298 272 265 290 235 300" fill="none" stroke="var(--white)" stroke-width="2.5" opacity=".85"/>
  </svg>

  <div class="holder">
    <p class="holder-name">EMPLOYEE NAME</p>
    <p class="holder-role">Managing Director</p>
  </div>

  <div class="brand">
    <span class="brand-dot"></span>
    <p class="brand-name">KM Rivergate<br>Fitness</p>
  </div>
  <p class="slogan"><span>Healthy mind, Healthy body</span><span>Ultimate lifestyle</span></p>

  <ul class="contacts">
    <li class="address">PO Box 418, Harlow Street,</li>
    <li class="address">Australia</li>
    <li>0400 318 552
      <svg viewBox="0 0 12 12"><path d="M3 1l2 2.5-1.2 1.2c.6 1.3 1.6 2.3 2.9 2.9L7.9 6.4 10.4 8.5 9.3 10.8C5 10.5 1.5 7 1.2 2.7Z" fill="currentColor"/></svg></li>
    <li>kemal@rivergatefit.com.au
      <svg viewBox="0 0 12 12"><rect x="1" y="2.5" width="10" height="7" rx="1" fill="currentColor"/><path d="M1.5 3l4.5 3.5L10.5 3" fill="none" stroke="var(--blue-mid)" stroke-width="1"/></svg></li>
    <li>www.rivergatefit.com.au
      <svg viewBox="0 0 12 12"><circle cx="6" cy="6" r="4.8" fill="none" stroke="currentColor" stroke-width="1.2"/><path d="M1.2 6h9.6M6 1.2c-2.4 2.6-2.4 7 0 9.6M6 1.2c2.4 2.6 2.4 7 0 9.6" fill="none" stroke="currentColor" stroke-width=".9"/></svg></li>
    <li>rivergatefit.social
      <svg viewBox="0 0 12 12"><circle cx="6" cy="6" r="5" fill="currentColor"/></svg></li>
    <li>@rivergatefit
      <svg viewBox="0 0 12 12"><circle cx="6" cy="6" r="5" fill="currentColor"/></svg></li>
  </ul>
</section>

<section class="card card-back" aria-label="Business card back">
  <h1 class="back-brand">KM Rivergate<span>Fitness</span></h1>
  <p class="offer">Show this card to receive 50% off your first 30min pt session</p>
  <p class="valid">Valid to one user only</p>
  <p class="services-label">we offer</p>
  <p class="services">Personal training, Bootcamps, Pilates, Nutrition</p>
  <p class="website">www.rivergatefit.com.au</p>
</section>

</body>
</html>
```